House Cleaning company in need of handout re-designs

We are looking to create a 2 sided, full color, 6" x 4" handout that promotes the company www.dustly.com

We have one in existence that performed well, but find it too busy and would like another one designed to test performance (please see the attached files for original design). We are looking for one additional design, however depending on quality of work submitted we will select up to 5 designs.

We are looking for clean designs the will improve performance and you are 'carte blanche' on the design. That said, please ensure the following elements are present:

1) Space for an offer (i.e $39 for 3 hours of cleaning) with an expiry date.
2) Unique URL
3) Promo Code
4) Phone Number
5) The tagline of "Let Dustly handle it" is present.
6) Logo
7) Brand colors are maintained

Also, please highlight the following:

*Eco-Friendly Cleaning Services
*Fully-Screened Cleaning Experts
*60-point checklist
*Easy Online Booking Process

Thank you.

House Cleaning

```html
<!DOCTYPE html>
<html lang="en">
<head>
<meta charset="utf-8">
<title>Dustly – Book a Trusted House Cleaning Professional</title>
<link rel="stylesheet" href="https://fonts.googleapis.com/css2?family=Oswald:wght@300;400;500&family=Roboto:wght@400;500&display=swap">
<style>
  :root {
    --teal: #2fa89c;
    --teal-light: #5fc0b4;
    --orange: #ee7a43;
    --orange-soft: #f2915f;
    --ink: #1d2a2a;
    --white: #ffffff;
    --room-light: #f4f3f1;
    --room-mid: #e4e2de;
  }
  * { margin: 0; padding: 0; box-sizing: border-box; }
  html, body { width: 1200px; height: 800px; overflow: hidden; background: var(--white); }
  .handout {
    position: relative;
    width: 1200px;
    height: 800px;
    overflow: hidden;
    font-family: "Oswald", "Arial Narrow", sans-serif;
  }
  .room-backdrop {
    position: absolute; inset: 0;
    background: linear-gradient(100deg, var(--room-mid) 0%, var(--room-light) 35%, #fbfaf8 60%, var(--room-mid) 100%);
  }
  .cleaner-photo {
    position: absolute; right: 0; top: 0;
    width: 400px; height: 800px;
    background: linear-gradient(180deg, #efeeeb 0%, #f6f5f2 28%, #bfe3dc 45%, var(--teal-light) 70%, #3aa99c 100%);
    opacity: .9;
  }
  .photo-circle {
    position: absolute;
    border-radius: 50%;
    border: 5px solid var(--white);
    box-shadow: 0 2px 8px rgba(0,0,0,.15);
  }
  .photo-circle.window {
    left: 45px; top: 118px; width: 212px; height: 212px;
    background: linear-gradient(135deg, #cfe6f5 0%, #e9f3f8 45%, #3fa99a 100%);
  }
  .photo-circle.family {
    left: 266px; top: 38px; width: 268px; height: 268px;
    background: radial-gradient(circle at 50% 55%, #e8d3c2 0%, #d9c4b4 40%, #8a7566 100%);
  }
  .brand-block {
    position: absolute; left: 560px; top: 140px;
  }
  .brand-name {
    font-weight: 400;
    font-size: 68px;
    line-height: 1;
    color: var(--orange);
    letter-spacing: 1px;
  }
  .tagline {
    margin-top: 10px;
    font-family: "Roboto", Arial, sans-serif;
    font-size: 20px;
    color: var(--teal);
  }
  .feature-list {
    position: absolute; left: 52px; top: 338px;
    width: 540px;
    list-style: none;
    display: grid;
    grid-template-columns: 1fr 1fr;
    row-gap: 8px;
    font-family: "Roboto", Arial, sans-serif;
    font-size: 16px;
    color: var(--ink);
  }
  .feature-list li { display: flex; align-items: center; gap: 8px; }
  .headline {
    position: absolute; left: 48px; top: 398px;
    line-height: 1;
  }
  .headline .lead {
    display: block;
    font-weight: 400;
    font-size: 84px;
    color: var(--teal);
    letter-spacing: 1px;
  }
  .headline .main {
    display: block;
    font-weight: 500;
    font-size: 64px;
    line-height: 1.12;
    color: var(--orange);
    margin-top: 16px;
  }
  .offer-badge {
    position: absolute; left: 605px; top: 400px;
    width: 270px; height: 270px;
  }
  .offer-text {
    position: absolute; left: 605px; top: 400px;
    width: 270px; height: 270px;
    display: flex; flex-direction: column; align-items: center; justify-content: center;
    color: var(--white);
    text-align: center;
    transform: rotate(-16deg);
    line-height: 1.08;
  }
  .offer-text .price { font-size: 46px; font-weight: 500; }
  .offer-text .detail { font-size: 19px; font-weight: 300; }
  .offer-text .expiry { font-size: 14px; font-weight: 400; margin-top: 4px; }
  .cta-bar {
    position: absolute; top: 700px;
    height: 64px;
  }
  .cta-bar .tab {
    position: absolute; left: 14px; top: 10px; right: 0;
    height: 44px;
    border-radius: 0 12px 12px 0;
    display: flex; align-items: center; justify-content: center;
    font-family: "Roboto", Arial, sans-serif;
    font-size: 22px;
    color: var(--ink);
  }
  .cta-bar svg { position: absolute; left: 0; top: 0; }
  .cta-bar.book { left: 30px; width: 342px; }
  .cta-bar.web { left: 410px; width: 342px; }
  .cta-bar.call { left: 790px; width: 342px; }
  .tab.teal { background: var(--teal-light); opacity: .92; }
  .tab.orange { background: var(--orange-soft); opacity: .95; }
  .cta-bar.book .tab { font-family: "Oswald", sans-serif; font-size: 24px; font-weight: 300; letter-spacing: .5px; }
</style>
</head>
<body>
<main class="handout">
  <div class="room-backdrop" role="img" aria-label="Bright, airy living room with white curtains"></div>
  <div class="cleaner-photo" role="img" aria-label="Smiling cleaning professional in a teal apron holding a mop and a bucket of supplies"></div>
  <div class="photo-circle window" role="img" aria-label="Cleaner wiping a window with a yellow cloth"></div>
  <div class="photo-circle family" role="img" aria-label="Happy family of four at home"></div>

  <div class="brand-block">
    <div class="brand-name">Dustly.com</div>
    <p class="tagline">Let Dustly handle it</p>
  </div>

  <ul class="feature-list">
    <li><svg width="18" height="18" viewBox="0 0 18 18" aria-hidden="true"><circle cx="9" cy="9" r="9" fill="#2fa89c"/><path d="M5 9.5l2.6 2.6L13 6.5" fill="none" stroke="#fff" stroke-width="2"/></svg>Eco-Friendly Cleaning Services</li>
    <li><svg width="18" height="18" viewBox="0 0 18 18" aria-hidden="true"><circle cx="9" cy="9" r="9" fill="#2fa89c"/><path d="M5 9.5l2.6 2.6L13 6.5" fill="none" stroke="#fff" stroke-width="2"/></svg>Fully-Screened Cleaning Experts</li>
    <li><svg width="18" height="18" viewBox="0 0 18 18" aria-hidden="true"><circle cx="9" cy="9" r="9" fill="#2fa89c"/><path d="M5 9.5l2.6 2.6L13 6.5" fill="none" stroke="#fff" stroke-width="2"/></svg>60-Point Checklist</li>
    <li><svg width="18" height="18" viewBox="0 0 18 18" aria-hidden="true"><circle cx="9" cy="9" r="9" fill="#2fa89c"/><path d="M5 9.5l2.6 2.6L13 6.5" fill="none" stroke="#fff" stroke-width="2"/></svg>Easy Online Booking Process</li>
  </ul>

  <h1 class="headline">
    <span class="lead">BOOK A TRUSTED</span>
    <span class="main">HOUSE CLEANING<br>PROFESSIONAL TODAY</span>
  </h1>

  <svg class="offer-badge" viewBox="0 0 270 270" aria-hidden="true">
    <g fill="#f08350" opacity=".92">
      <circle cx="135" cy="135" r="112"/>
      <circle cx="135" cy="25" r="24"/><circle cx="190" cy="40" r="24"/>
      <circle cx="230" cy="80" r="24"/><circle cx="245" cy="135" r="24"/>
      <circle cx="230" cy="190" r="24"/><circle cx="190" cy="230" r="24"/>
      <circle cx="135" cy="245" r="24"/><circle cx="80" cy="230" r="24"/>
      <circle cx="40" cy="190" r="24"/><circle cx="25" cy="135" r="24"/>
      <circle cx="40" cy="80" r="24"/><circle cx="80" cy="40" r="24"/>
    </g>
  </svg>
  <div class="offer-text">
    <span class="price">$39</span>
    <span class="detail">CLEANING FOR<br>3 HOURS<br>A $105 VALUE! USE<br>PROMO CODE: CA39</span>
    <span class="expiry">OFFER EXPIRES 12/31/2025</span>
  </div>

  <div class="cta-bar book">
    <div class="tab teal">BOOK NOW AT</div>
    <svg width="36" height="64" viewBox="0 0 36 64" aria-hidden="true"><polygon points="0,0 36,32 0,64" fill="#ee7a43"/></svg>
  </div>
  <div class="cta-bar web">
    <div class="tab orange">www.dustly.com/ca39</div>
    <svg width="36" height="64" viewBox="0 0 36 64" aria-hidden="true"><polygon points="0,0 36,32 0,64" fill="#2fa89c"/></svg>
  </div>
  <div class="cta-bar call">
    <div class="tab teal">or call 1-800-8DUSTLY</div>
    <svg width="36" height="64" viewBox="0 0 36 64" aria-hidden="true"><polygon points="0,0 36,32 0,64" fill="#ee7a43"/></svg>
  </div>
</main>
</body>
</html>
```